Attorney Website Design

I need a top quality attorney website layout designed. Here are some examples of what I feel are great websites:
http://www.quellmarstonseparationlaw.com/
http://www.vandriclegalgroup.com/
http://www.pobelaw.com/
http://www.harrowvaleaccusedcounselhq.com/
http://www.tzlegal.com/
http://www.brookhollowtrialjusticeoffice.com/
http://www.orvynchargedcounsel.com/
http://www.tzlegal.com/
What we like about these sites:
• The different layers
• Subtle designs, textures, curves
• 3 dimensional
• Floating effects
• Prominent phone number
• Location of Areas of Practice
• Request A Consultation Prominent
• Right side bar with practice areas
• Badges
• Clear Calls to Action
• Dynamic/Staying Top navigation when you scroll
The project will be for a home page and then also an interior page (should be similar to home page).
Updates
I want to make it understood I am looking for a design which is not a typical "template" site which I can find anywhere for $50. This budget and project is for a "Custom" website design. Please submit designs similar in quality to the samples links I have posted. Creativity is a MUST! The best way to explain this is, I want a design that I can feel it unique and original, not something that looks like 95% of all websites out there.
Neil
I just wanted everyone to know that so far I am not to pleased with any of the designs. I am not looking for cut/pasting of other peoples websites but ORIGINAL and CREATIVE work.
Reason: Weekend + Holiday extension.
Reason: Need more designs
Industry/Entity Type
Attorney

```html
<!DOCTYPE html>
<html lang="en">
<head>
<meta charset="utf-8">
<title>Kestrow Attorney at Law</title>
<link href="https://fonts.googleapis.com/css2?family=Open+Sans:ital,wght@0,300;0,400;0,600;0,700;1,400&display=swap" rel="stylesheet">
<style>
:root{
  --header:#2b2c2e;
  --nav:#c9c9c9;
  --nav-active:#6f6f6f;
  --band:#6a6a6a;
  --panel:#777777;
  --field:#5d5d5d;
  --field-line:#9a9a9a;
  --gold:#f2c12e;
  --gold-box:#b8963d;
  --text-light:#eeeeee;
  --text-mute:#d6d6d6;
  --testimonial:#2e2e2e;
  --newsletter:#7b7b7b;
  --footer:#222222;
}
*{box-sizing:border-box;margin:0;padding:0}
html,body{width:673px;height:1200px;overflow:hidden}
body{font-family:"Open Sans",sans-serif;background:var(--band);position:relative;color:var(--text-light)}
.abs{position:absolute}

.site-header{left:0;top:0;width:673px;height:98px;background:var(--header)}
.brand{left:58px;top:13px;display:flex;align-items:center;gap:8px}
.brand-mark{width:32px;height:34px;background:var(--gold)}
.brand-name{font-size:30px;font-weight:600;color:#fff;letter-spacing:.5px;line-height:1}
.brand-tag{left:99px;top:48px;font-size:7px;letter-spacing:5px;color:#bbb}
.call{left:400px;top:20px;text-align:right;width:103px}
.call small{display:block;font-size:10px;line-height:13px;color:#fff}
.call strong{display:block;font-size:12px;line-height:15px;font-weight:600;color:var(--gold);white-space:nowrap}
.phone-box{left:510px;top:22px;width:24px;height:22px;background:#e6e6e6;border-radius:3px}
.social{left:546px;top:22px;height:24px;display:flex;align-items:center;gap:12px;padding-left:12px;border-left:1px solid #444}
.social span{width:12px;height:12px;border-radius:50%;background:#e6e6e6}

.main-nav{left:56px;top:72px;width:561px;height:26px;background:var(--nav);display:flex;align-items:center}
.main-nav a{font-size:8.4px;font-weight:600;color:#333;text-decoration:none;padding:0 13px;height:26px;line-height:26px;border-right:1px solid #b3b3b3}
.main-nav a.active{background:var(--nav-active);color:#fff;padding:0 15px}
.search{margin-left:auto;margin-right:8px;width:88px;height:17px;background:#5f5f5f;border:1px solid #888;font-size:8px;color:#bbb;line-height:15px;padding-left:6px;position:relative}

.hero{left:56px;top:98px;width:561px;height:226px;background:linear-gradient(90deg,#6e6e6e 0%,#9a9a9a 35%,#4d4d4d 70%,#2f2f2f 100%)}
.hero-title{left:358px;top:150px;width:210px;text-align:center;font-size:20px;font-weight:700;line-height:25px;color:#fff;text-transform:uppercase}
.cta{left:359px;top:203px;width:203px;height:24px;background:var(--gold);color:#222;font-size:10.5px;font-weight:700;text-align:center;line-height:24px}
.dots{left:315px;top:303px;display:flex;gap:6px}
.dots span{width:6px;height:6px;border-radius:50%;background:#ddd}
.dots span:first-child{background:none;border:1px solid #ddd}

.feature-panel{left:56px;top:324px;width:561px;height:128px;background:var(--panel);box-shadow:0 6px 8px rgba(0,0,0,.35)}
.section-title{font-size:12.5px;font-weight:600;color:#fff}
.attorney{width:78px;height:76px;background:#cfcfcf;padding:2px}
.attorney .photo{width:74px;height:58px;background:linear-gradient(#8a8a8a,#5a5a5a)}
.attorney p{font-size:7.6px;color:#333;text-align:center;line-height:14px}
.divider-v{left:338px;top:340px;width:1px;height:98px;background:#8a8a8a}
.field{width:123px;height:19px;background:var(--field);border:1px solid var(--field-line);font-size:7.6px;color:#ccc;line-height:17px;padding-left:7px}
.submit{left:558px;top:414px;width:47px;height:18px;background:#cfcfcf;color:#333;font-size:8.6px;font-weight:700;text-align:center;line-height:18px}

.copy{font-size:7.6px;line-height:12.8px;color:var(--text-mute)}
.video{left:349px;top:504px;width:122px;height:72px;background:linear-gradient(135deg,#555,#2d2d2d)}
.play{left:402px;top:531px;width:17px;height:17px;border-radius:50%;background:rgba(255,255,255,.55)}
.divider-h{left:56px;top:632px;width:416px;height:1px;background:#7c7c7c}
.badge{top:660px;height:30px;background:#8a8a8a}

.practice-box{left:481px;top:498px;width:136px;height:206px;background:var(--gold-box);padding:4px}
.practice-box ul{border:1px solid #8a6e24;height:100%;list-style:none;padding:10px 0 0 14px}
.practice-box li{font-size:8.6px;color:#222;line-height:20px}
.practice-box li::before{content:"•";margin-right:6px;font-size:7px}

.testimonials{left:0;top:724px;width:673px;height:166px;background:var(--testimonial)}
.avatar{left:70px;top:784px;width:72px;height:72px;border-radius:50%;background:radial-gradient(#bdbdbd,#8e8e8e);border:3px solid #fff}
.quote{left:153px;top:789px;width:450px;font-size:8px;font-style:italic;line-height:14px;color:#ddd}
.quote-name{left:153px;top:834px;font-size:8.4px;color:var(--gold)}

.newsletter{left:0;top:890px;width:673px;height:64px;background:var(--newsletter)}
.nl-title{left:95px;top:909px;font-size:17px;line-height:22px;font-weight:300;color:#fff;white-space:nowrap}
.nl-field{top:911px;width:148px;height:19px;background:#5a5a5a;font-size:8px;color:#ccc;line-height:19px;padding-left:8px}
.subscribe{left:521px;top:911px;width:55px;height:19px;background:var(--gold);color:#222;font-size:9px;font-weight:700;text-align:center;line-height:19px}

.map{left:0;top:954px;width:673px;height:166px;background:linear-gradient(135deg,#cfcfcf,#b9b9b9)}
.site-footer{left:0;top:1120px;width:673px;height:80px;background:var(--footer);text-align:center}
.footer-links{margin-top:25px;font-size:7.8px;color:#bbb}
.footer-links span{margin:0 5px;color:#666}
.legal{margin-top:10px;font-size:7.8px;color:#aaa}
</style>
</head>
<body>

<header class="site-header abs"></header>
<div class="brand abs"><span class="brand-mark"></span><span class="brand-name">KESTROW</span></div>
<div class="brand-tag abs">ATTORNEY AT LAW</div>
<div class="call abs"><small>Call us</small><strong>555 014 2287</strong></div>
<div class="phone-box abs">
  <svg width="24" height="22" viewBox="0 0 24 22"><path d="M8 6c1 0 2 2 2 3s-1 1-1 2 2 3 3 3 1-1 2-1 3 1 3 2-1 2-3 2c-4 0-8-4-8-8 0-2 1-3 2-3z" fill="#333"/></svg>
</div>
<div class="social abs"><span></span><span></span><span></span></div>

<nav class="main-nav abs">
  <a class="active">HOME</a><a>OUR FIRM</a><a>PRACTISE AREAS</a><a>ATTORNEYS</a><a>CLIENT REVIEWS</a><a>CONTACT US</a>
  <div class="search">Search
    <svg class="abs" style="right:3px;top:2px" width="11" height="11" viewBox="0 0 11 11"><circle cx="4.5" cy="4.5" r="3.3" stroke="#ddd" fill="none" stroke-width="1.3"/><path d="M7 7l3 3" stroke="#ddd" stroke-width="1.4"/></svg>
  </div>
</nav>

<div class="hero abs" role="img" aria-label="Smiling attorney in a suit in front of a city skyline"></div>
<h1 class="hero-title abs">Pellentesque non augue elementum</h1>
<div class="cta abs">CLICK HERE FOR CALL TO ACTION</div>
<div class="dots abs"><span></span><span></span><span></span><span></span></div>

<section class="feature-panel abs"></section>
<h2 class="section-title abs" style="left:69px;top:334px">Our Attorneys</h2>
<div class="attorney abs" style="left:70px;top:358px"><div class="photo" role="img" aria-label="Attorney portrait"></div><p>Ravel Dunn</p></div>
<div class="attorney abs" style="left:158px;top:358px"><div class="photo" role="img" aria-label="Attorney portrait"></div><p>Ravel Dunn</p></div>
<div class="attorney abs" style="left:246px;top:358px"><div class="photo" role="img" aria-label="Attorney portrait"></div><p>Ravel Dunn</p></div>
<div class="divider-v abs"></div>
<h2 class="section-title abs" style="left:351px;top:334px">Request a Consultation</h2>
<div class="field abs" style="left:352px;top:358px">Name</div>
<div class="field abs" style="left:481px;top:358px">E-mail</div>
<div class="field abs" style="left:352px;top:385px">Phone</div>
<div class="field abs" style="left:481px;top:385px">About your case</div>
<div class="submit abs">SUBMIT</div>

<h2 class="section-title abs" style="left:58px;top:472px">Welcome to Kestrow</h2>
<p class="copy abs" style="left:58px;top:502px;width:280px">Proin vitae quam id justo pulvinar commodo. Curabitur varius interdum est, sed dapibus elit commodo eget. Pellentesque a ornare magna. Mauris id iacu lis arcu, vel consequat tellus. Maecenas eget euismod diam. Pellentesque habitant morbi tristique senectus et netus et malesuada fames ac turpis eges tas. Fusce porta nulla in magna pretium pharetra sit amet sit amet eros. Donec a elementum augue. Praesent ornare ante a aliquam egestas.</p>
<div class="video abs" role="img" aria-label="Video still of a justice statue holding scales"></div>
<div class="play abs"></div>
<p class="copy abs" style="left:58px;top:586px;width:414px">Suspendisse eleifend varius sagittis. Donec viverra diam at velit tempor commodo. Aliquam erat volutpat. Praesent dignissim dui nec lorem suscipit iaculis.</p>
<div class="divider-h abs"></div>
<div class="badge abs" style="left:62px;width:70px"></div>
<div class="badge abs" style="left:170px;width:62px"></div>
<div class="badge abs" style="left:262px;width:38px;border-radius:50%;height:38px;top:656px"></div>
<div class="badge abs" style="left:344px;width:38px;border-radius:50%;height:38px;top:656px"></div>
<div class="badge abs" style="left:412px;width:52px"></div>

<h2 class="section-title abs" style="left:482px;top:472px">Practise Areas</h2>
<aside class="practice-box abs">
  <ul>
    <li>Family Law</li><li>Business Law</li><li>Accident &amp; Injuries</li><li>Cross Border Disputes</li><li>Contract Disputes</li><li>Real Estate Litigation</li><li>Family Law</li><li>Business Law</li><li>Accident &amp; Injuries</li>
  </ul>
</aside>

<section class="testimonials abs" role="img" aria-label="Dark backdrop of a justice statue"></section>
<h2 class="section-title abs" style="left:0;width:673px;text-align:center;top:757px">Client’s Testimonials</h2>
<svg class="abs" style="left:22px;top:811px" width="12" height="18" viewBox="0 0 12 18"><path d="M10 2L3 9l7 7" stroke="#888" stroke-width="2" fill="none"/></svg>
<svg class="abs" style="left:638px;top:811px" width="12" height="18" viewBox="0 0 12 18"><path d="M2 2l7 7-7 7" stroke="#888" stroke-width="2" fill="none"/></svg>
<div class="avatar abs" role="img" aria-label="Client portrait"></div>
<p class="quote abs">“ Nam a malesuada libero. Duis sodales et libero vel interdum. Interdum et malesuada fames ac ante ipsum primis in faucibus. Donec lobortis dui tortor, eu lobortis felis mattis nec. Sed justo quam, luctus eu mauris eget, euismod dapibus sem. Sed tempus feugiat ante, at ornare libero volutpat sed. Maecenas quis magna magna. ”</p>
<div class="quote-name abs">Tobin - Team Name</div>

<section class="newsletter abs"></section>
<h2 class="nl-title abs">NEWS LETTER</h2>
<div class="nl-field abs" style="left:216px">Name</div>
<div class="nl-field abs" style="left:369px">Email ID</div>
<div class="subscribe abs">Subscribe</div>

<div class="map abs" role="img" aria-label="Street map of the office location"></div>

<footer class="site-footer abs">
  <div class="footer-links">Home<span>/</span>Our Firm<span>/</span>Practise Areas<span>/</span>Attorneys<span>/</span>Client Reviews<span>/</span>Contact us</div>
  <div class="legal">Copyright © 2014 Kestrow. All rights reserved.</div>
</footer>

</body>
</html>
```